Business card design needed

Looking for an innovative design that portrays a professional image for our company. We are a structural steel erection, EWP and crane hire company. We are looking at having business and contact details on front of card and perhaps a list of what we hire on the back of the card. Our company machine colours are royal blue and silver at present but would be open to change with our cards...
Updates
We are looking for double sided designs due to the amount of information required on the card
The Logo uploaded if the logo we have been using, however our company name has changed to just "Stoneridge Lifting Works". I have uploaded the image just for ideas...
Reason: Allowing more time for more design submissions
Reason: Want more dedigns
Target Market(s)
Construction/Industrial
Industry/Entity Type
Structural Steel
Contact Information for Business Card
Business Name: Stoneridge Lifting Works
Specialising in Structural Steel Erection, Equipment & Crane Hire
Address: 27 Carvell Street, Mondarra Q 4612
Site Contact: Danny Pruett - 0491 637 205 - dan@slwlifting.com
Office Contact: Leoni Marsh - 0437 918 542 - leoni@slwlifting.com
We hire Forklifts, Telehandlers, Scissor-lifts, Boom-lifts, 3T Mini Cranes, 16T/20T Kelvo, Prime mover with extendable trailer (13.5-22m), Qualified Boilermakers,Riggers and Dogman.
Logo Text
Stoneridge Lifting Works or SLW
Logo styles of interest
Emblem Logo
Look and feel

```html
<!DOCTYPE html>
<html lang="en">
<head>
<meta charset="utf-8">
<title>Stoneridge Lifting Works – Business Cards</title>
<link href="https://fonts.googleapis.com/css2?family=Oswald:wght@300;400&display=swap" rel="stylesheet">
<style>
  :root {
    --page: #ffffff;
    --ink: #0b0b0b;
    --white: #ffffff;
    --royal: #2b2bd6;
    --silver-light: #e4e6e6;
    --silver-mid: #b9bcbd;
    --silver-dark: #8e9293;
    --list-text: #eef0ff;
  }
  html, body {
    margin: 0;
    padding: 0;
    width: 1200px;
    height: 1000px;
    overflow: hidden;
    background: var(--page);
  }
  .canvas {
    position: relative;
    width: 1200px;
    height: 1000px;
    font-family: "Oswald", "Arial Narrow", sans-serif;
  }
  .card {
    position: absolute;
    width: 600px;
    height: 370px;
    overflow: hidden;
    background:
      radial-gradient(ellipse 60% 45% at 35% 20%, rgba(255,255,255,0.55), transparent 70%),
      radial-gradient(ellipse 50% 40% at 80% 85%, rgba(255,255,255,0.35), transparent 70%),
      linear-gradient(160deg, var(--silver-light) 0%, var(--silver-mid) 45%, var(--silver-dark) 75%, var(--silver-light) 100%);
  }
  .card--front { left: 151px; top: 97px; }
  .card--back {
    left: 455px;
    top: 520px;
    transform: rotate(-19.7deg);
  }
  .front-panel {
    position: absolute;
    inset: 0;
  }
  .contact-name {
    position: absolute;
    left: 45px;
    top: 62px;
    margin: 0;
    color: var(--white);
    font-weight: 300;
    font-size: 34px;
    line-height: 1;
    letter-spacing: -0.5px;
  }
  .contact-role {
    position: absolute;
    left: 45px;
    top: 106px;
    margin: 0;
    color: var(--royal);
    font-weight: 300;
    font-size: 17px;
  }
  .contact-list {
    position: absolute;
    left: 48px;
    top: 210px;
    margin: 0;
    padding: 0;
    list-style: none;
    color: var(--white);
    font-weight: 300;
    font-size: 14.5px;
  }
  .contact-list li {
    display: flex;
    align-items: center;
    height: 27px;
  }
  .contact-list svg {
    width: 16px;
    height: 16px;
    margin-right: 18px;
    fill: var(--white);
  }
  .brand {
    position: absolute;
    display: flex;
    flex-direction: column;
    align-items: center;
    text-align: center;
  }
  .card--front .brand { left: 260px; top: 52px; width: 320px; }
  .card--back .brand { left: 140px; top: 70px; width: 320px; }
  .brand-mark {
    width: 26px;
    height: 26px;
    background: var(--ink);
    margin-bottom: 14px;
  }
  .brand-name {
    margin: 0;
    color: var(--ink);
    font-weight: 400;
    font-size: 27px;
    line-height: 1.1;
  }
  .brand-tagline {
    margin: 14px 0 0;
    color: var(--royal);
    font-weight: 300;
    font-size: 15px;
    line-height: 1.35;
  }
  .hire-list {
    position: absolute;
    left: 40px;
    right: 40px;
    top: 270px;
    margin: 0;
    text-align: center;
    color: var(--list-text);
    font-weight: 400;
    font-size: 14px;
    line-height: 1.3;
    text-shadow: 0 0 2px rgba(40,40,60,0.8), 1px 1px 2px rgba(40,40,60,0.6);
  }
</style>
</head>
<body>
<main class="canvas">

  <section class="card card--front" aria-label="Business card front">
    <svg class="front-panel" viewBox="0 0 600 370" width="600" height="370" aria-hidden="true">
      <path d="M0 0 H240 C268 0 262 55 250 95 C236 140 222 180 248 230 C282 296 312 340 348 370 H0 Z" fill="var(--ink)"/>
    </svg>

    <h1 class="contact-name">Danny Pruett</h1>
    <p class="contact-role">Site Contact</p>

    <ul class="contact-list">
      <li>
        <svg viewBox="0 0 16 16" aria-hidden="true"><path d="M3.5 1.5l2.5 2.8-1.4 1.9c.8 1.9 2.3 3.4 4.2 4.2l1.9-1.4 2.8 2.5-1.4 2.4C7 13.4 2.6 9 1.5 2.9z"/></svg>
        0491 637 205
      </li>
      <li>
        <svg viewBox="0 0 16 16" aria-hidden="true"><path d="M1 3h14v1.5L8 9 1 4.5z M1 6.3l7 4.5 7-4.5V13H1z"/></svg>
        dan@slwlifting.com
      </li>
      <li>
        <svg viewBox="0 0 16 16" aria-hidden="true"><path d="M6.5 9.5l3-3" stroke="#fff" stroke-width="1.8" fill="none"/><path d="M7 4.5l1.8-1.8a2.8 2.8 0 014 4L11 8.5M9 11.5l-1.8 1.8a2.8 2.8 0 01-4-4L5 7.5" stroke="#fff" stroke-width="1.8" fill="none"/></svg>
        www.slwlifting.com
      </li>
      <li>
        <svg viewBox="0 0 16 16" aria-hidden="true"><path d="M8 .8a5 5 0 015 5c0 3.6-5 9.4-5 9.4S3 9.4 3 5.8a5 5 0 015-5zm0 3a2 2 0 100 4 2 2 0 000-4z"/></svg>
        27 Carvell Street, Mondarra Q 4612
      </li>
    </ul>

    <div class="brand">
      <span class="brand-mark" aria-hidden="true"></span>
      <p class="brand-name">Stoneridge Lifting Works</p>
      <p class="brand-tagline">Specialising in Structural Steel Erection,<br>Equipment &amp; Crane Hire</p>
    </div>
  </section>

  <section class="card card--back" aria-label="Business card back">
    <div class="brand">
      <span class="brand-mark" aria-hidden="true"></span>
      <p class="brand-name">Stoneridge Lifting Works</p>
      <p class="brand-tagline">Specialising in Structural Steel Erection,<br>Equipment &amp; Crane Hire</p>
    </div>
    <p class="hire-list">We hire Forklifts, Telehandlers, Scissor-lifts, Boom-lifts, 3T Mini Cranes, 16T/20T Kelvo, Prime mover with extendable trailer (13.5-22m), Qualified Boilermakers,Riggers and Dogman.</p>
  </section>

</main>
</body>
</html>
```